New business needs it's first website designed and coded for Wordpress

This is a new website for a new business. The business is called The Remote Tech Specialist (TRTS). The business is based across multiple countries with the goal of providing workers in the Philippines opportunities to find work in international companies based in Australia, Singapore and New Zealand. The target market for TRTS is large enterprises (initially in Australia) looking for well legally structured business that knows how to recruit the top IT professionals and ensure that they are happy, all compliance, taxes and legals and professionally done and all services contracts are local to ensure enforceability.

We are looking for 10 pages (6 templates) for the website as follows:
Home
About Us
Services
Work from home full-timers
Work from office full-times
Work from home contractors
Work from office contractors
Careers Job Search
Employers Contact Us
Candidates Register your interest

Target Market(s)

IT Professionals in the Philippines & large enterprises in Australia, Singapore and New Zealand

Industry/Entity Type

IT Recruitment

Coding

Coded - Design and coding required

Number of Pages Required

5+ page

Requirements
Must have
• Please based style off logo file attached.

```html
<!DOCTYPE html>
<html lang="en">
<head>
<meta charset="utf-8">
<title>The Remote Tech Specialist – Find Your Perfect Job</title>
<link rel="stylesheet" href="https://fonts.googleapis.com/css2?family=Syncopate:wght@700&family=Lato:wght@400;700;900&display=swap">
<style>
:root{
  --blue:#0aa9e8;
  --ink:#111;
  --muted:#777;
  --hero:#f4f0ee;
  --line:#e6e6e6;
  --white:#fff;
}
*{box-sizing:border-box;margin:0;padding:0}
html,body{width:1200px;height:4089px;overflow:hidden}
body{position:relative;background:var(--white);font-family:"Lato",sans-serif;color:var(--ink);letter-spacing:.06em}
.abs{position:absolute}
.display{font-family:"Syncopate",sans-serif;font-weight:700;text-transform:uppercase;letter-spacing:.04em;line-height:1;white-space:nowrap}
.accent{color:var(--blue)}
.btn{position:absolute;display:flex;align-items:center;gap:14px;background:var(--blue);color:#fff;font-weight:700;font-size:13px;padding:0 6px 0 12px;height:40px;border-radius:2px;white-space:nowrap}
.btn .arrow{width:42px;height:30px;background:#fff;border-radius:2px;display:flex;align-items:center;justify-content:center}
.photo{position:absolute}
.brand{display:flex;align-items:center;gap:8px;font-weight:900;font-size:34px;color:var(--blue);letter-spacing:.02em}
.brand .mark{width:20px;height:20px;background:var(--blue)}
.topinfo{font-size:13px;color:#333;display:flex;align-items:center;gap:8px;white-space:nowrap}
.topinfo svg{width:20px;height:20px}
.nav{display:flex;font-size:13px;align-items:center;white-space:nowrap}
.nav a{color:#222;text-decoration:none}
.nav .active{background:var(--blue);color:#fff;padding:4px 10px;font-weight:700}
.hero{position:absolute;left:0;top:108px;width:1200px;height:616px;background:var(--hero)}
.float-card{position:absolute;background:#fff;box-shadow:0 4px 16px rgba(0,0,0,.08);border-radius:3px}
.stats{position:absolute;left:0;top:724px;width:1200px;height:101px;background:var(--blue);color:#fff}
.stat{position:absolute;top:28px;display:flex;align-items:center;gap:16px;white-space:nowrap}
.stat b{font-family:"Syncopate",sans-serif;font-size:40px;font-weight:700;letter-spacing:.02em}
.stat span{font-size:14px;line-height:22px}
.cat{position:absolute;width:235px;height:80px;background:#fff;box-shadow:0 2px 10px rgba(0,0,0,.07);display:flex;align-items:center;gap:14px;padding-left:12px;white-space:nowrap}
.cat .ic{width:44px;height:44px;border:2px solid var(--blue);border-radius:50%;flex:none;opacity:.8}
.cat h4{font-size:15px;font-weight:700}
.cat p{font-size:11px;color:var(--muted);margin-top:6px}
.cat.on{background:var(--blue);color:#fff}
.cat.on .ic{border-color:#fff}
.cat.on p{color:#e6f7ff}
.about{position:absolute;left:0;top:1314px;width:1200px;height:492px;background:var(--hero)}
.label{font-size:16px;font-weight:700;letter-spacing:.1em}
.job{position:absolute;width:314px;height:252px;background:#fff;box-shadow:0 2px 12px rgba(0,0,0,.08);white-space:nowrap}
.job .logo{position:absolute;left:20px;top:28px;width:46px;height:46px;border-radius:4px}
.job .co{position:absolute;left:80px;top:30px;font-size:16px;font-weight:700}
.job .loc{position:absolute;left:80px;top:54px;font-size:13px;color:var(--muted)}
.job .tag{position:absolute;right:2px;top:14px;background:#dff3fc;color:var(--blue);font-size:11px;padding:3px 12px;border-radius:10px}
.job hr{position:absolute;left:22px;right:22px;top:94px;border:0;border-top:1px solid var(--line)}
.job .role{position:absolute;left:22px;top:118px;font-size:13px;font-weight:700}
.job .pay{position:absolute;left:26px;top:144px;font-size:12px;color:var(--blue)}
.job .posted{position:absolute;left:24px;top:196px;font-size:12px;color:#555}
.career{position:absolute;left:0;top:2622px;width:1200px;height:362px;background:linear-gradient(90deg,#1c2226 0%,#2a3035 45%,#4a4f52 70%,#3a4146 100%);color:#fff}
.field{position:absolute;left:600px;width:486px;background:#fff;box-shadow:0 2px 10px rgba(0,0,0,.08);font-size:13px;color:#666;padding:20px 22px}
.footer{position:absolute;left:0;top:3653px;width:1200px;height:436px;background:var(--blue);color:#fff}
.fcol{position:absolute;top:184px;white-space:nowrap}
.fcol h5{font-size:20px;font-weight:700;margin-bottom:12px}
.fcol li{list-style:none;font-size:16px;line-height:27px}
.fcol .row{display:flex;align-items:center;gap:10px;font-size:14px;margin-bottom:22px}
.fcol .social .row{font-size:16px;margin-bottom:14px}
.sq{width:18px;height:18px;background:#fff;border-radius:2px;flex:none}
</style>
</head>
<body>

<header>
  <div class="abs brand" style="left:110px;top:8px"><span class="mark"></span>TRTS</div>
  <div class="abs topinfo" style="left:482px;top:14px">
    <svg viewBox="0 0 20 20"><rect width="20" height="20" rx="3" fill="#bbb"/><path d="M10 4a4 4 0 0 0-4 4c0 3 4 8 4 8s4-5 4-8a4 4 0 0 0-4-4z" fill="#fff"/></svg>
    48 Harbour Lane, Sydney 2000</div>
  <div class="abs topinfo" style="left:734px;top:14px">
    <svg viewBox="0 0 20 20"><rect width="20" height="20" rx="3" fill="#bbb"/><path d="M6 5l2 0 1 3-1.5 1a7 7 0 0 0 3.5 3.5l1-1.5 3 1v2a1 1 0 0 1-1 1A10 10 0 0 1 5 6a1 1 0 0 1 1-1z" fill="#fff"/></svg>
    +61 2 5550 0147</div>
  <div class="abs topinfo" style="left:960px;top:14px">
    <svg viewBox="0 0 20 20"><rect width="20" height="20" rx="3" fill="#bbb"/><path d="M4 6h12v8H4zM4 6l6 5 6-5" fill="none" stroke="#fff" stroke-width="1.5"/></svg>
    info@trts.com</div>
  <nav class="abs nav" style="left:111px;top:71px">
    <a class="active" href="#">Home</a>
    <a href="#" style="margin-left:32px">About Us</a>
    <a href="#" style="margin-left:42px">Services</a>
    <a href="#" style="margin-left:42px">Works ⌄</a>
    <a href="#" style="margin-left:42px">Careers</a>
    <a href="#" style="margin-left:52px">Contact Us</a>
  </nav>
  <svg class="abs" style="left:880px;top:68px" width="22" height="22" viewBox="0 0 22 22"><circle cx="9" cy="9" r="7" fill="none" stroke="#222" stroke-width="2"/><path d="M14 14l6 6" stroke="#222" stroke-width="2"/></svg>
  <div class="btn" style="left:921px;top:62px">Register Now <span class="arrow"><svg width="18" height="12" viewBox="0 0 18 12"><path d="M0 6h16M11 1l5 5-5 5" fill="none" stroke="#111" stroke-width="1.6"/></svg></span></div>
</header>

<section class="hero">
  <p class="abs" style="left:110px;top:94px;font-size:13px;font-weight:700;letter-spacing:.05em">STAY CONNECT TO GET UPCOMING JOB TRTS</p>
  <h1 class="abs display" style="left:108px;top:134px;font-size:50px;line-height:61px">Find Your<br><span class="accent">Perfect Job</span><br>Platform</h1>
  <div class="btn" style="left:110px;top:327px">Find Job <span class="arrow"><svg width="18" height="12" viewBox="0 0 18 12"><path d="M0 6h16M11 1l5 5-5 5" fill="none" stroke="#111" stroke-width="1.6"/></svg></span></div>
  <div class="abs" role="img" aria-label="Row of regular user portraits" style="left:110px;top:400px;width:204px;height:80px">
    <span class="abs" style="left:0;top:24px;width:40px;height:40px;border-radius:50%;background:#cfc6c0;border:3px solid #fff"></span>
    <span class="abs" style="left:30px;top:18px;width:50px;height:50px;border-radius:50%;background:#a8b6c2;border:3px solid #fff"></span>
    <span class="abs" style="left:70px;top:12px;width:60px;height:60px;border-radius:50%;background:#d6b79a;border:3px solid #fff"></span>
    <span class="abs" style="left:118px;top:0;width:84px;height:84px;border-radius:50%;background:#a9c9b1;border:4px solid #fff"></span>
  </div>
  <p class="abs" style="left:323px;top:432px;font-size:16px;font-weight:700">Regular Users</p>
  <div class="photo" role="img" aria-label="Smiling young man in glasses holding a laptop" style="left:600px;top:90px;width:540px;height:526px;background:radial-gradient(ellipse at 45% 55%,#d9c2ae 0%,#c7d3dc 45%,var(--hero) 75%)"></div>
  <div class="float-card" style="left:884px;top:162px;width:279px;height:127px">
    <svg class="abs" style="left:30px;top:20px" width="26" height="32" viewBox="0 0 26 32"><path d="M13 0a12 12 0 0 0-12 12c0 9 12 20 12 20s12-11 12-20A12 12 0 0 0 13 0z" fill="#e5141b"/><circle cx="13" cy="12" r="5" fill="#fff"/></svg>
    <p class="abs" style="left:68px;top:26px;font-size:16px">Australia</p>
    <p class="abs" style="left:38px;top:66px;font-size:16px;white-space:nowrap">Senior Product Designer</p>
    <p class="abs" style="left:38px;top:92px;font-size:11px;color:#555">12500-15000/month</p>
  </div>
  <div class="float-card" style="left:568px;top:320px;width:230px;height:70px">
    <svg class="abs" style="left:16px;top:22px" width="28" height="28" viewBox="0 0 28 28"><circle cx="14" cy="14" r="14" fill="#111"/><path d="M8 10h12v9H8zM8 10l6 5 6-5" fill="none" stroke="#fff" stroke-width="1.5"/></svg>
    <p class="abs" style="left:58px;top:22px;font-size:11px;color:#555;line-height:18px;white-space:nowrap">Marlo is applied into<br>Your Job</p>
  </div>
  <div class="float-card" style="left:505px;top:457px;width:230px;height:70px">
    <svg class="abs" style="left:16px;top:18px" width="26" height="32" viewBox="0 0 26 32"><path d="M2 1h15l7 7v23H2z" fill="none" stroke="#39b54a" stroke-width="2"/><path d="M13 24V12M8 17l5-5 5 5" fill="none" stroke="#39b54a" stroke-width="2"/></svg>
    <p class="abs" style="left:56px;top:16px;font-size:15px">Upload Your Cv</p>
    <p class="abs" style="left:56px;top:40px;font-size:11px;color:#555;white-space:nowrap">It only take a few Seconds</p>
  </div>
</section>

<section class="stats">
  <div class="stat" style="left:110px"><b>10K</b><span>Job Poster<br>Every Month</span></div>
  <div class="stat" style="left:368px"><b>25+</b><span>Million Daily<br>Active Users</span></div>
  <div class="stat" style="left:628px"><b>12K</b><span>Trusted By<br>Company</span></div>
  <div class="stat" style="left:889px"><b>10M</b><span>Over 20 Million<br>Stories Shared</span></div>
</section>

<section>
  <p class="abs label" style="left:110px;top:910px">SERVICES</p>
  <h2 class="abs display" style="left:110px;top:948px;font-size:34px">Popular <span class="accent">Job Categories</span></h2>
  <div class="cat" style="left:111px;top:1003px"><span class="ic"></span><div><h4>Data Analysts</h4><p>(2 Open Positions)</p></div></div>
  <div class="cat" style="left:357px;top:1003px"><span class="ic"></span><div><h4>Software Developer</h4><p>(2 Open Positions)</p></div></div>
  <div class="cat" style="left:603px;top:1003px"><span class="ic"></span><div><h4>Network Engineers</h4><p>(2 Open Positions)</p></div></div>
  <div class="cat" style="left:849px;top:1003px"><span class="ic"></span><div><h4>IT Project Manger</h4><p>(2 Open Positions)</p></div></div>
  <div class="cat" style="left:111px;top:1092px"><span class="ic"></span><div><h4>Architecture</h4><p>(2 Open Positions)</p></div></div>
  <div class="cat" style="left:357px;top:1092px"><span class="ic"></span><div><h4>Data Scientist</h4><p>(2 Open Positions)</p></div></div>
  <div class="cat on" style="left:603px;top:1092px"><span class="ic"></span><div><h4>Cloud Architect</h4><p>(2 Open Positions)</p></div></div>
  <div class="cat" style="left:849px;top:1092px"><span class="ic"></span><div><h4>Data Science</h4><p>(2 Open Positions)</p></div></div>
  <div class="btn" style="left:111px;top:1187px">View All <span class="arrow"><svg width="18" height="12" viewBox="0 0 18 12"><path d="M0 6h16M11 1l5 5-5 5" fill="none" stroke="#111" stroke-width="1.6"/></svg></span></div>
</section>

<section class="about">
  <div class="photo" role="img" aria-label="Two colleagues working together at a laptop" style="left:114px;top:44px;width:216px;height:286px;background:linear-gradient(160deg,#d8dde0,#9aa3a8 60%,#e6e8e9)"></div>
  <div class="abs" style="left:113px;top:346px;width:220px;height:83px;background:#000;color:#fff;display:flex;align-items:center;justify-content:center;text-align:center;font-size:24px;font-weight:700;line-height:31px">10K Happy<br>Customers</div>
  <div class="abs" style="left:352px;top:51px;width:219px;height:82px;background:var(--blue);color:#fff;display:flex;align-items:center;justify-content:center;text-align:center;font-size:24px;font-weight:700;line-height:31px">10+ Years<br>Experience</div>
  <div class="photo" role="img" aria-label="Two women reviewing work on a laptop" style="left:354px;top:146px;width:217px;height:286px;background:linear-gradient(160deg,#cfd4d6,#8d8a86 55%,#e1dfdc)"></div>
  <p class="abs label" style="left:647px;top:62px">ABOUT US</p>
  <h2 class="abs display" style="left:645px;top:100px;font-size:44px">Who <span class="accent">We Are</span></h2>
  <p class="abs" style="left:646px;top:166px;width:440px;font-size:12.5px;line-height:29px;color:#555">Lorem ipsum dolor sit amet, consectetur adipiscing elit, sed do eiusmod tempor incididunt ut labore et dolore magna aliqua. Ut enim ad minim veniam, quis nostrud exercitation ullamco laboris nisi ut aliquip ex ea commodo consequat. Duis aute irure dolor in reprehenderit in voluptate velit esse cillum dolore eu fugiat nulla pariatur.</p>
  <div class="btn" style="left:644px;top:356px">Read More <span class="arrow"><svg width="18" height="12" viewBox="0 0 18 12"><path d="M0 6h16M11 1l5 5-5 5" fill="none" stroke="#111" stroke-width="1.6"/></svg></span></div>
</section>

<section>
  <p class="abs label" style="left:111px;top:1889px">POPULAR JOBS</p>
  <h2 class="abs display" style="left:111px;top:1926px;font-size:34px">Find Your <span class="accent">Favourite Jobs</span></h2>
  <div class="btn" style="left:940px;top:1902px">View All <span class="arrow" style="margin-left:16px"><svg width="18" height="12" viewBox="0 0 18 12"><path d="M0 6h16M11 1l5 5-5 5" fill="none" stroke="#111" stroke-width="1.6"/></svg></span></div>

  <div class="job" style="left:111px;top:2017px"><span class="logo" style="background:#6a4fc8"></span><span class="co">Northsuite</span><span class="loc">Singapore</span><span class="tag">Full Time</span><hr><span class="role">IT Project Manager</span><span class="pay">20000/Month</span><span class="posted">Posted 1 Year ago</span></div>
  <div class="job" style="left:441px;top:2017px"><span class="logo" style="background:#1e7fd6"></span><span class="co">Marketing</span><span class="loc">Australia</span><span class="tag">Full Time</span><hr><span class="role">Data Analysts</span><span class="pay">25000/Month</span><span class="posted">Posted 3 Months ago</span></div>
  <div class="job" style="left:771px;top:2017px"><span class="logo" style="background:#14c44a"></span><span class="co">Northsuite</span><span class="loc">New Zealand</span><span class="tag">Part Time</span><hr><span class="role">Graphic Designer</span><span class="pay">5000/Month</span><span class="posted">Posted 1 Year ago</span></div>
  <div class="job" style="left:111px;top:2282px"><span class="logo" style="background:#ee2b4d"></span><span class="co">Tinkerlane</span><span class="loc">Australia</span><span class="tag">Full Time</span><hr><span class="role">Cloud Architect</span><span class="pay">20000/Month</span><span class="posted">Posted 2 Weeks &nbsp;ago</span></div>
  <div class="job" style="left:441px;top:2282px"><span class="logo" style="background:#f7d60f"></span><span class="co">Northsuite</span><span class="loc">New Zeland</span><span class="tag">Contractor</span><hr><span class="role">Data Science</span><span class="pay">20000/Month</span><span class="posted">Posted 1 Month ago</span></div>
  <div class="job" style="left:771px;top:2282px"><span class="logo" style="background:#f4efe3"></span><span class="co">Brightfix Labs</span><span class="loc">Singapore</span><span class="tag">Part Time</span><hr><span class="role">IT Project Manager</span><span class="pay">20000/Month</span><span class="posted">Posted 15 Days ago</span></div>
</section>

<section class="career">
  <div class="photo" role="img" aria-label="Businessman and businesswoman looking at a laptop in an office" style="left:620px;top:0;width:580px;height:362px;background:linear-gradient(100deg,rgba(0,0,0,0),#7d8288 40%,#c8c2b8 60%,#3c4a66 85%)"></div>
  <p class="abs" style="left:111px;top:44px;font-size:17px;font-weight:700;letter-spacing:.1em">CAREER</p>
  <h2 class="abs display" style="left:110px;top:72px;font-size:36px;line-height:51px">Looking For Post<br>Or <span class="accent">Get A Job?</span></h2>
  <p class="abs" style="left:111px;top:178px;width:560px;font-size:14px;line-height:27px">Sed ut perspiciatis unde omnis iste natus error sit voluptatem accusantium doloremque laudantium, totam rem aperiam, eaque ipsa quae ab illo inventore veritatis et quasi architecto .</p>
  <div class="btn" style="left:111px;top:286px">Satrt Your Career <span class="arrow"><svg width="18" height="12" viewBox="0 0 18 12"><path d="M0 6h16M11 1l5 5-5 5" fill="none" stroke="#111" stroke-width="1.6"/></svg></span></div>
</section>

<section>
  <div class="photo" role="img" aria-label="Laptop showing a job search page" style="left:111px;top:3071px;width:444px;height:492px;background:linear-gradient(160deg,#e9e9e9,#b9bcbf 55%,#5a5e62)"></div>
  <h2 class="abs display" style="left:600px;top:3072px;font-size:42px">Get In <span class="accent">Touch</span></h2>
  <div class="field" style="top:3146px;height:55px">Name</div>
  <div class="field" style="top:3219px;height:55px">Email Address</div>
  <div class="field" style="top:3291px;height:56px">Phone</div>
  <div class="field" style="top:3364px;height:140px">Message</div>
  <div class="btn" style="left:600px;top:3527px">Submit Now <span class="arrow"><svg width="18" height="12" viewBox="0 0 18 12"><path d="M0 6h16M11 1l5 5-5 5" fill="none" stroke="#111" stroke-width="1.6"/></svg></span></div>
</section>

<footer class="footer">
  <div class="abs" style="left:111px;top:66px;display:flex;align-items:center;gap:12px;font-weight:900;font-size:58px;color:#fff;letter-spacing:.02em"><span style="width:28px;height:28px;background:#fff"></span>TRTS</div>
  <div class="abs" style="left:562px;top:69px;width:524px;height:57px;background:#fff;display:flex;align-items:center">
    <span style="padding-left:20px;font-size:13px;color:#666;flex:1">Enter Email Addres</span>
    <span style="background:#000;color:#fff;height:57px;display:flex;align-items:center;gap:14px;padding:0 8px 0 16px;font-size:13px;font-weight:700;white-space:nowrap">Submit Now <span style="width:38px;height:30px;background:#fff;display:flex;align-items:center;justify-content:center"><svg width="18" height="12" viewBox="0 0 18 12"><path d="M0 6h16M11 1l5 5-5 5" fill="none" stroke="#111" stroke-width="1.6"/></svg></span></span>
  </div>
  <div class="fcol" style="left:111px"><h5>Quick Links</h5><ul><li>Home</li><li>About Us</li><li>Services</li><li>Works</li><li>Careers</li><li>Contact Us</li></ul></div>
  <div class="fcol" style="left:352px"><h5>Help Links</h5><ul><li>Privacy Policy</li><li>Terms &amp; Conditions</li><li>FAQ's</li><li>Support</li><li>Help</li></ul></div>
  <div class="fcol" style="left:600px"><h5>Help Links</h5>
    <div class="row" style="margin-top:16px"><span class="sq"></span>48 Harbour Lane, Sydney 2000</div>
    <div class="row"><span class="sq"></span>+61 2 5550 0147</div>
    <div class="row"><span class="sq"></span>info@trts.com</div>
  </div>
  <div class="fcol social" style="left:900px"><h5>Follow Us</h5>
    <div class="row" style="margin-top:8px"><span class="sq"></span><u>Community</u></div>
    <div class="row"><span class="sq"></span>Gallery</div>
    <div class="row"><span class="sq"></span>Updates</div>
    <div class="row"><span class="sq"></span>Network</div>
  </div>
  <div class="abs" style="left:111px;top:388px;width:975px;border-top:1px solid rgba(255,255,255,.6)"></div>
  <p class="abs" style="left:0;top:406px;width:1200px;text-align:center;font-size:12px">© 2024 &nbsp;The Remote Tech Specialist..All Rights Reserved</p>
</footer>

</body>
</html>
```